Re-design / re-work of existing website

Need to re-design a website so it's easy for me as a user to update/add pictures and change descriptions.

If possible, would there be a way to display LodgeVu calendars? We have 3 cottages and it would be ideal to have each cottage with pics on one page along with a readonly version of the LodgeVu calendar plugin (if such a thing exists) so that visitors to the site can see what is available and what is not.

Existing site: http://tqlodgings.net

```html
<!DOCTYPE html>
<html lang="en">
<head>
<meta charset="utf-8">
<title>Tamarack Quay Cottages</title>
<link rel="stylesheet" href="https://fonts.googleapis.com/css2?family=Playfair+Display:ital,wght@1,500;1,600&family=Poppins:wght@400;500;600&display=swap">
<style>
:root{
  --accent:#f2a516;
  --accent-dark:#e08e00;
  --ink:#222;
  --text:#555;
  --cream:#fcf1e7;
  --footer:#2a2a2a;
  --line:#e6e6e6;
  --white:#fff;
}
*{box-sizing:border-box;margin:0;padding:0}
html,body{width:1200px;height:5362px;overflow:hidden}
body{font-family:"Poppins",sans-serif;color:var(--text);background:var(--white);position:relative}
.serif{font-family:"Playfair Display",serif;font-style:italic;font-weight:500;color:var(--ink)}
.eyebrow{font-size:13px;letter-spacing:4px;color:var(--accent);text-transform:uppercase;font-weight:500}
.btn{display:inline-flex;align-items:center;gap:6px;background:var(--accent);color:#fff;font-size:13px;font-weight:600;text-transform:uppercase;border-radius:20px;padding:0 18px;height:36px}
.btn .dot{width:11px;height:11px;border-radius:50%;background:#fff;position:relative}
.btn .dot::after{content:"";position:absolute;left:3px;top:3px;border-left:5px solid var(--accent);border-top:2.5px solid transparent;border-bottom:2.5px solid transparent}
.photo{display:block}
section,header,footer{position:absolute;left:0;width:1200px}

/* header */
.site-header{top:0;height:78px;background:#fff}
.brand{position:absolute;left:100px;top:24px;font-weight:600;font-size:18px;color:var(--ink);display:flex;align-items:center;gap:8px}
.brand .mark{width:16px;height:16px;border:2px solid var(--ink);border-radius:50%}
.nav{position:absolute;left:363px;top:28px;display:flex;gap:26px;font-size:14px;color:var(--ink);text-transform:uppercase;font-weight:500}
.nav .active{color:var(--accent);border-bottom:2px solid var(--accent);padding-bottom:6px}
.site-header .btn{position:absolute;left:963px;top:20px;height:36px}

/* hero */
.hero{top:78px;height:625px;background:linear-gradient(160deg,#a87a4f 0%,#7b4f2e 45%,#4a3020 100%)}
.hero h1{position:absolute;top:218px;width:100%;text-align:center;font-size:56px;color:#fff}
.booking{position:absolute;left:156px;top:313px;width:890px;height:46px;background:#fff;border-radius:24px;display:flex;align-items:center;font-size:11px;color:var(--ink);text-transform:uppercase;overflow:hidden}
.booking .field{flex:1;display:flex;align-items:center;justify-content:center;gap:8px;height:100%;border-right:1px solid var(--line)}
.booking .field svg{width:13px;height:13px}
.booking .caret{border-top:5px solid var(--ink);border-left:4px solid transparent;border-right:4px solid transparent;margin-left:10px}
.booking .find{width:185px;height:100%;background:var(--accent);color:#fff;font-weight:600;font-size:13px;display:flex;align-items:center;justify-content:center;gap:6px}
.hero .help{position:absolute;top:382px;width:100%;text-align:center;font-size:13px;color:#fff}

/* welcome */
.welcome{top:703px;height:637px;background:var(--cream)}
.welcome .eyebrow{position:absolute;left:100px;top:76px}
.welcome h2{position:absolute;left:100px;top:102px;font-size:38px;line-height:46px;width:420px}
.welcome p{position:absolute;left:100px;top:203px;width:430px;font-size:12.4px;line-height:27.5px;text-align:justify}
.welcome .btn{position:absolute;left:100px;top:523px}
.welcome .aerial{position:absolute;left:566px;top:79px;width:272px;height:383px;background:linear-gradient(180deg,#6c7a62,#8d8c80 55%,#4d5a48)}
.welcome .interior{position:absolute;left:755px;top:179px;width:278px;height:381px;background:linear-gradient(180deg,#8c9aa0,#c9c4b8 55%,#b7946c)}
.welcome .years{position:absolute;left:558px;top:419px;width:150px;height:42px;background:#3a3a3a;color:#fff;display:flex;align-items:center;gap:8px;padding-left:16px}
.welcome .years b{font-size:24px;font-weight:500}
.welcome .years span{font-size:9px;line-height:10px;text-transform:uppercase}
.welcome .sketch{position:absolute;left:1040px;top:0;width:160px;height:460px;background:linear-gradient(180deg,rgba(190,170,120,.12),rgba(190,170,120,.22))}

/* cottages */
.cottages{top:1340px;height:680px}
.center-head{position:absolute;width:100%;text-align:center}
.cottages .eyebrow{top:60px}
.cottages h2{top:86px;font-size:36px}
.cottage{position:absolute;top:149px;width:314px}
.cottage .photo{width:314px;height:287px}
.cottage h3{font-size:28px;margin-top:12px}
.cottage p{font-size:14px;line-height:26px;margin-top:4px;color:var(--text)}
.cottage .btn{margin-top:12px;height:34px}

/* space */
.space{top:2020px;height:500px;background:linear-gradient(100deg,#b98a5e 0%,#d9d3c8 35%,#c7bfb2 55%,#8f6a48 100%)}
.card{position:absolute;background:#fff;box-shadow:0 6px 24px rgba(0,0,0,.15)}
.space .card{left:653px;top:81px;width:447px;height:337px;padding:34px 28px}
.card h2{font-size:36px}
.card p{font-size:12.4px;line-height:27px;margin-top:10px}
.card .btn{margin-top:14px}

/* testimonials */
.testimonials{top:2520px;height:760px}
.testimonials .eyebrow{top:58px}
.testimonials h2{top:84px;font-size:36px}
.review{position:absolute;top:151px;width:474px;height:522px;background:#fff;box-shadow:0 4px 18px rgba(0,0,0,.1)}
.review .photo{width:474px;height:274px}
.review .stars{position:absolute;left:26px;top:296px;color:var(--accent);font-size:20px;letter-spacing:2px}
.review .quote{position:absolute;right:30px;top:290px;font-family:"Playfair Display",serif;font-size:64px;line-height:64px;color:var(--accent)}
.review p{position:absolute;left:26px;top:338px;width:422px;font-size:12.4px;line-height:26px;font-style:italic;text-align:justify}
.review .who{position:absolute;left:26px;top:454px;display:flex;align-items:center;gap:14px;font-size:15px;font-weight:600;color:var(--ink);text-transform:uppercase}
.review .avatar{width:52px;height:52px;border-radius:50%;background:#d9d9d9}
.arrow{position:absolute;top:2927px;width:38px;height:38px;border-radius:50%;border:1px solid #ccc;background:#fff;display:flex;align-items:center;justify-content:center}

/* amenities */
.amenities{top:3280px;height:500px;background:linear-gradient(90deg,#c9b9a3 0%,#b7ab99 40%,#5a82a6 70%,#9a8c7c 100%)}
.amenities .card{left:108px;top:75px;width:454px;height:354px;padding:20px 26px;box-shadow:none}

/* explore */
.explore{top:3780px;height:850px}
.explore .eyebrow{top:66px}
.explore h2{top:92px;font-size:38px}
.spot{position:absolute;width:317px;text-align:center}
.spot .photo{width:317px;height:260px}
.spot h3{font-size:18px;margin-top:12px}

/* map */
.map{top:4630px;height:350px;background:linear-gradient(180deg,#e6e6e6,#d6d6d6)}
.map .pin{position:absolute;left:422px;top:152px}

/* footer */
.site-footer{top:4980px;height:382px;background:var(--footer);color:#ddd}
.footer-brand{position:absolute;left:100px;top:96px;font-size:22px;font-weight:600;color:#fff;display:flex;align-items:center;gap:10px}
.footer-brand .mark{width:18px;height:18px;border:2px solid #fff;border-radius:50%}
.socials{position:absolute;left:112px;top:178px;display:flex;gap:14px}
.socials span{width:40px;height:40px;border:1px solid #fff;border-radius:50%}
.fcol{position:absolute;top:68px}
.fcol h4{font-family:"Playfair Display",serif;font-style:italic;font-weight:500;font-size:20px;color:#fff;margin-bottom:14px}
.fcol li{list-style:none;font-size:13.5px;line-height:28px}
.fcol .row{display:flex;gap:8px;font-size:13.5px;line-height:20px;margin-bottom:16px}
.fcol .row svg{flex:none;margin-top:3px}
.fcol p{font-size:13.5px;line-height:22px;width:265px}
.email-box{width:265px;height:38px;border:1px solid #999;border-radius:20px;margin-top:14px;padding-left:20px;font-size:13px;line-height:36px;color:#fff}
.fcol .btn{width:265px;justify-content:center;margin-top:12px;height:38px}
.copyright{position:absolute;left:0;top:304px;width:100%;border-top:1px solid #444;padding-top:18px;font-size:13px;text-align:center;color:#ccc}
.copyright::before{content:none}
</style>
</head>
<body>

<header class="site-header">
  <div class="brand"><span class="mark"></span>Tamarack Quay</div>
  <nav class="nav">
    <span class="active">Home</span><span>Our Cottages</span><span>Adventures</span><span>Getting Here</span><span>Contact Us</span>
  </nav>
  <span class="btn">Book Now <span class="dot"></span></span>
</header>

<section class="hero" role="img" aria-label="Cottage living room with wood panelled walls, leather sofa and wood stove">
  <h1 class="serif">Tamarack Quay Cottages</h1>
  <div class="booking">
    <div class="field"><svg viewBox="0 0 14 14"><rect x="1" y="2" width="12" height="11" fill="none" stroke="#222"/><line x1="1" y1="5" x2="13" y2="5" stroke="#222"/></svg>Arrival<span class="caret"></span></div>
    <div class="field"><svg viewBox="0 0 14 14"><rect x="1" y="2" width="12" height="11" fill="none" stroke="#222"/><line x1="1" y1="5" x2="13" y2="5" stroke="#222"/></svg>Departure<span class="caret"></span></div>
    <div class="field"><svg viewBox="0 0 14 14"><circle cx="7" cy="4" r="3" fill="none" stroke="#222"/><path d="M1 13c0-4 12-4 12 0" fill="none" stroke="#222"/></svg>2 Adults<span class="caret"></span></div>
    <div class="field"><svg viewBox="0 0 14 14"><circle cx="7" cy="4" r="3" fill="none" stroke="#222"/><path d="M1 13c0-4 12-4 12 0" fill="none" stroke="#222"/></svg>0 Children<span class="caret"></span></div>
    <div class="field"><svg viewBox="0 0 14 14"><rect x="1" y="4" width="12" height="7" fill="none" stroke="#222"/><line x1="1" y1="8" x2="13" y2="8" stroke="#222"/></svg>1 Rooms<span class="caret"></span></div>
    <div class="find">Find a Cottages <span class="dot" style="width:11px;height:11px;border-radius:50%;background:#fff"></span></div>
  </div>
  <p class="help">Need Help? Call +1 647 555 0148</p>
</section>

<section class="welcome">
  <div class="sketch" role="img" aria-label="Faint line drawing of pine trees and rocky shoreline"></div>
  <p class="eyebrow">Welcome to Tamarack Quay Cottages!</p>
  <h2 class="serif">Killarney/ French River, Ontario, Canada</h2>
  <p>Come and enjoy life on the water! This south facing property promises long sun filled days and a gorgeous sunrise, along with unlimited family fun and relaxation. The location is perfect, and guests will undoubtedly enjoy everything this Killarney /French River destination has to offer. The rock outcroppings and majestic topography along the pristine waters is a sight to behold. Make Tamarack Quay cottages your hub to visit the various brag worthy destinations, such as The Killarney, French River and Grundy Lake provincial parks, or just relax and kick back at the cottages, that have it all. For a quaint town experience, and last-minute shopping, drive down via a scenic drive to the towns</p>
  <span class="btn">Get Your Reservation <span class="dot"></span></span>
  <div class="aerial photo" role="img" aria-label="Aerial view of a white cottage on rocky shoreline surrounded by trees"></div>
  <div class="interior photo" role="img" aria-label="Bright dining nook with a white table and a lake painting on the wall"></div>
  <div class="years"><b>30+</b><span>Years of<br>Experience</span></div>
</section>

<section class="cottages">
  <p class="eyebrow center-head" style="top:60px">Best Cottages!</p>
  <h2 class="serif center-head" style="top:86px;font-size:36px">Blend Yourself With Nature</h2>
  <article class="cottage" style="left:100px">
    <div class="photo" role="img" aria-label="The Aspen kitchen and dining area with wood floors" style="background:linear-gradient(180deg,#c8bda9,#9a6a44 70%,#7a3e2a)"></div>
    <h3 class="serif">The Aspen</h3>
    <p>3 Bedroom, 1 Bathroom with Large Kitchen and Living Space</p>
    <span class="btn">Book Now <span class="dot"></span></span>
  </article>
  <article class="cottage" style="left:443px">
    <div class="photo" role="img" aria-label="The Birch living room with lake view windows" style="background:linear-gradient(180deg,#d8d6d0,#bdb2a0 60%,#8e7155)"></div>
    <h3 class="serif">The Birch</h3>
    <p>3 Bedroom, 2 Bathrooms with Large Kitchen and Living Space</p>
    <span class="btn">Book Now <span class="dot"></span></span>
  </article>
  <article class="cottage" style="left:786px">
    <div class="photo" role="img" aria-label="The Cedar living room with sofa and lake view" style="background:linear-gradient(180deg,#a3a79f,#8f8a7e 60%,#a07a56)"></div>
    <h3 class="serif">The Cedar</h3>
    <p>2 Bedroom, 1 Bathroom with Large Kitchen and Living Space</p>
    <span class="btn">Book Now <span class="dot"></span></span>
  </article>
</section>

<section class="space" role="img" aria-label="Open plan cottage kitchen and living area with wood panelling">
  <div class="card">
    <h2 class="serif">The Space</h2>
    <p>Welcome to Tamarack Quay Cottages! This quaint 3 cottage oasis is situated in a woodland setting yet right off Tamarack Quay Road, on the shores of beautiful Badger Lake. Our cottages are a little over 3 hours' drive from Toronto, and about an hour's drive from Sudbury. Badger lake is a calm and quiet lake with little water traffic, which makes it a very safe destination for kids, and all kinds of water sports and activities.</p>
    <span class="btn">Book Now <span class="dot"></span></span>
  </div>
</section>

<section class="testimonials">
  <p class="eyebrow center-head" style="top:58px">Testimonials</p>
  <h2 class="serif center-head" style="top:84px;font-size:36px">Our Happy Clients</h2>
  <article class="review" style="left:108px">
    <div class="photo" role="img" aria-label="White cottage kitchen with wood floors" style="background:linear-gradient(180deg,#e4e2de,#c9c3b8 60%,#9c7448)"></div>
    <div class="stars">★★★★★</div><div class="quote">“</div>
    <p>Lorem ipsum dolor sit amet, cetudipiscing elit, sed do eiusmod tempor incididunt ut labore et dolore mana aliqua. Quis ipsum suspendisse ultricravida. Risus commodo viverra maecenas accumsan lacus vel facilisis.</p>
    <div class="who"><span class="avatar" role="img" aria-label="Guest portrait"></span>John Smith</div>
  </article>
  <article class="review" style="left:618px">
    <div class="photo" role="img" aria-label="Wood panelled living room with plaid armchairs" style="background:linear-gradient(180deg,#c49a6a,#a5764c 60%,#6e4a33)"></div>
    <div class="stars">★★★★★</div><div class="quote">“</div>
    <p>Lorem ipsum dolor sit amet, cetudipiscing elit, sed do eiusmod tempor incididunt ut labore et dolore mana aliqua. Quis ipsum suspendisse ultricravida. Risus commodo viverra maecenas accumsan lacus vel facilisis.</p>
    <div class="who"><span class="avatar" role="img" aria-label="Guest portrait"></span>John Smith</div>
  </article>
</section>
<span class="arrow" style="left:43px"><svg width="16" height="10" viewBox="0 0 16 10"><path d="M15 5H1M5 1L1 5l4 4" fill="none" stroke="#333" stroke-width="1.3"/></svg></span>
<span class="arrow" style="left:1117px"><svg width="16" height="10" viewBox="0 0 16 10"><path d="M1 5h14M11 1l4 4-4 4" fill="none" stroke="#333" stroke-width="1.3"/></svg></span>

<section class="amenities" role="img" aria-label="Dining area with pendant lights, a blue armchair and window views">
  <div class="card">
    <h2 class="serif">Our Amenities</h2>
    <p>Tamarack Quay Cottages have fully self-contained kitchens, clean and hygenic washrooms, and option to select from our 3 cottages, The Aspen, The Birch and The Cedar. Free boat launch into badger lake from the property or go down to Tamarack Quay marina and step into the heart of French River Provincial Park. Each of our cottages is self-contained, each with its own fire pit, wrap around deck and dock. Rent one for yourself, or bring the whole gang and rent them all!</p>
    <span class="btn">Book Now <span class="dot"></span></span>
  </div>
</section>

<section class="explore">
  <p class="eyebrow center-head" style="top:66px">Explore</p>
  <h2 class="serif center-head" style="top:92px;font-size:38px">Things to Explore near Tamarack Quay Cottages</h2>
  <div class="spot" style="left:100px;top:164px"><div class="photo" role="img" aria-label="Modern lodge building lit at dusk" style="background:linear-gradient(180deg,#5b5a7e,#3a2f3a 60%,#b07a3a)"></div><h3 class="serif">River Bend Trading Post</h3></div>
  <div class="spot" style="left:442px;top:164px"><div class="photo" role="img" aria-label="Waterfall rapids between forested banks" style="background:linear-gradient(180deg,#a9c2d8,#4e6b3c 50%,#d8dcd8)"></div><h3 class="serif">Recollet Falls</h3></div>
  <div class="spot" style="left:783px;top:164px"><div class="photo" role="img" aria-label="Rustic trading post storefront with porch" style="background:linear-gradient(180deg,#d8d8d8,#6a4a3a 55%,#8a8276)"></div><h3 class="serif">River Bend Trading Post</h3></div>
  <div class="spot" style="left:100px;top:478px"><div class="photo" role="img" aria-label="Calm lake with pine covered islands" style="background:linear-gradient(180deg,#a9a8c2,#4a5a4a 55%,#7a8894)"></div><h3 class="serif">Killarney Provincial Park</h3></div>
  <div class="spot" style="left:442px;top:478px"><div class="photo" role="img" aria-label="Marina dock with colourful canoes" style="background:linear-gradient(180deg,#8a9aa0,#5a6a6a 50%,#a04a3a)"></div><h3 class="serif">Tamarack Quay Marina</h3></div>
  <div class="spot" style="left:783px;top:478px"><div class="photo" role="img" aria-label="Red lawn chairs on rocks at sunset by the lake" style="background:linear-gradient(180deg,#a7b4c4,#d9a890 50%,#5a5a50)"></div><h3 class="serif">Point Grondine Park</h3></div>
</section>

<section class="map" role="img" aria-label="Map of the lakes and roads around the cottages">
  <svg class="pin" width="22" height="30" viewBox="0 0 22 30"><path d="M11 29C4 19 1 15 1 10a10 10 0 0 1 20 0c0 5-3 9-10 19z" fill="#e53935"/><circle cx="11" cy="10" r="4" fill="#fff"/></svg>
</section>

<footer class="site-footer">
  <div class="footer-brand"><span class="mark"></span>Tamarack Quay</div>
  <div class="socials"><span></span><span></span><span></span><span></span></div>
  <div class="fcol" style="left:389px">
    <h4>Quick Links</h4>
    <ul><li>Home</li><li>Our Cottages</li><li>Adventures</li><li>Getting Here</li><li>Contact Us</li><li>Today's Weather</li><li>Policies</li></ul>
  </div>
  <div class="fcol" style="left:572px">
    <h4>Connect with us</h4>
    <div class="row"><svg width="12" height="16" viewBox="0 0 12 16"><path d="M6 15C2 10 1 8 1 5.5a5 5 0 0 1 10 0C11 8 10 10 6 15z" fill="#fff"/><circle cx="6" cy="5.5" r="2" fill="#2a2a2a"/></svg><span>2801 Tamarack Quay Road,<br>Killarney P0M 9Z9</span></div>
    <div class="row"><svg width="12" height="14" viewBox="0 0 12 14"><path d="M2 1l3 3-1.5 2a8 8 0 0 0 4 4L9.5 8.5l2 2.5-2 2C5 12 1 8 0.5 3z" fill="#fff"/></svg><span>Phone :<br>+1 647 555 0148</span></div>
    <div class="row"><svg width="13" height="10" viewBox="0 0 13 10"><rect x="0.5" y="0.5" width="12" height="9" fill="#fff"/><path d="M0.5 0.5l6 5 6-5" fill="none" stroke="#2a2a2a"/></svg><span>Email :<br>support@tqlodgings.net</span></div>
  </div>
  <div class="fcol" style="left:834px">
    <h4>Keep In Touch</h4>
    <p>Put yourself in the know and receive the most exclusive Deals &amp; Specials Events before anyone else</p>
    <div class="email-box">Email</div>
    <span class="btn">Subscribe <span class="dot"></span></span>
  </div>
  <p class="copyright">©Copyright 2023 Tamarack Quay Cottages. All Rights Reserved.</p>
</footer>

</body>
</html>
```